Keeep it up is our company motto. Need "keeep it up" sticker design for promotional pur...

I need a sticker design for my upstart company called Plovark which I like to describe as The Friendly Corvano Fellow of Inner Growth. I'm looking for a cleanly designed combination mark that joins together our logo (see uploaded file) and the phrase "keeep it up." The 3 E's stand for Everyday Earnest Effort. One or two colors maximum. The phrase may be split up vertically or horizontally and the logo may also be tweaked a bit if needed. Overall design should be simple and easily recognizable.

```html
<!DOCTYPE html>
<html lang="en">
<head>
<meta charset="utf-8">
<title>Keeep It Up Sticker</title>
<link rel="stylesheet" href="https://fonts.googleapis.com/css2?family=Ubuntu:wght@500&display=swap">
<style>
  :root {
    --stage: #ebebeb;
    --sticker-red: #d92f30;
    --band-dark: #333333;
    --ink-white: #ffffff;
  }
  html, body {
    margin: 0;
    padding: 0;
    width: 1200px;
    height: 675px;
    overflow: hidden;
    background: var(--stage);
  }
  .canvas {
    position: relative;
    width: 1200px;
    height: 675px;
  }
  .sticker {
    position: absolute;
    left: 320px;
    top: 57px;
    width: 560px;
    height: 560px;
  }
  .sticker-base { fill: var(--sticker-red); }
  .cut-line { fill: none; stroke: var(--ink-white); stroke-width: 1.6; }
  .band { fill: var(--band-dark); }
  .stem { fill: var(--ink-white); }
  .hairline { fill: none; stroke: var(--ink-white); stroke-width: 3; stroke-linecap: square; }
  .word {
    font-family: "Ubuntu", sans-serif;
    font-weight: 500;
    font-size: 82px;
    fill: var(--ink-white);
  }
  .brand-name {
    font-family: "Ubuntu", sans-serif;
    font-weight: 500;
    font-size: 22px;
    fill: var(--ink-white);
  }
  .brand-dot { fill: var(--ink-white); }
</style>
</head>
<body>
<main class="canvas">
  <svg class="sticker" viewBox="0 0 723 723" role="img" aria-label="Keeep it up sticker: Everyday Earnest Effort, Plovark">
    <defs>
      <clipPath id="sticker-shape">
        <rect width="723" height="723" rx="22"/>
      </clipPath>
    </defs>
    <g clip-path="url(#sticker-shape)">
      <rect class="sticker-base" width="723" height="723"/>
      <rect class="cut-line" x="13" y="12" width="697" height="699" rx="18"/>

      <!-- dark bands -->
      <rect class="band" x="40" y="0" width="80" height="723"/>
      <rect class="band" x="0" y="204" width="723" height="61"/>
      <rect class="band" x="0" y="313" width="723" height="53"/>
      <rect class="band" x="0" y="410" width="723" height="61"/>
      <rect class="band" x="0" y="600" width="723" height="78"/>

      <!-- K -->
      <g class="letter-k">
        <rect class="stem" x="40" y="85" width="36" height="78"/>
        <path class="hairline" d="M113 88 L76 125 L118 163"/>
      </g>
      <!-- E -->
      <g class="letter-e">
        <rect class="stem" x="40" y="188" width="36" height="78"/>
        <path class="hairline" d="M76 189.5 H110 M76 227 H105 M76 264.5 H110"/>
      </g>
      <!-- E -->
      <g class="letter-e">
        <rect class="stem" x="40" y="293" width="36" height="75"/>
        <path class="hairline" d="M76 294.5 H110 M76 330 H105 M76 366.5 H110"/>
      </g>
      <!-- E -->
      <g class="letter-e">
        <rect class="stem" x="40" y="393" width="36" height="78"/>
        <path class="hairline" d="M76 394.5 H110 M76 432 H105 M76 469.5 H110"/>
      </g>
      <!-- P -->
      <g class="letter-p">
        <rect class="stem" x="40" y="493" width="36" height="78"/>
        <path class="hairline" d="M76 494.5 H94 A24 24 0 0 1 94 542.5 H76"/>
      </g>
      <!-- I -->
      <rect class="stem" x="40" y="603" width="36" height="75"/>

      <!-- words -->
      <text class="word" x="121" y="265" textLength="287" lengthAdjust="spacingAndGlyphs">veryday</text>
      <text class="word" x="121" y="366" textLength="230" lengthAdjust="spacingAndGlyphs">arnest</text>
      <text class="word" x="121" y="471" textLength="180" lengthAdjust="spacingAndGlyphs">fford</text>

      <!-- T -->
      <rect class="stem" x="111" y="603" width="77" height="10"/>
      <rect class="stem" x="133" y="603" width="35" height="75"/>
      <!-- U -->
      <path class="stem" d="M246 603 H278 V645 A14 16 0 0 0 292 661 V678 A46 40 0 0 1 246 640 Z"/>
      <path class="hairline" d="M323 603 V640 A31 36 0 0 1 292 676"/>
      <!-- P -->
      <rect class="stem" x="353" y="603" width="33" height="75"/>
      <path class="hairline" d="M386 604.5 H398 A29 29 0 0 1 398 662.5 H386"/>

      <!-- brand name marks -->
      <g class="brand-mark">
        <circle class="brand-dot" cx="572" cy="127" r="7"/><text class="brand-name" x="584" y="135">Plovark</text>
        <circle class="brand-dot" cx="462" cy="235" r="7"/><text class="brand-name" x="474" y="243">Plovark</text>
        <circle class="brand-dot" cx="572" cy="292" r="7"/><text class="brand-name" x="584" y="300">Plovark</text>
        <circle class="brand-dot" cx="462" cy="384" r="7"/><text class="brand-name" x="474" y="392">Plovark</text>
        <circle class="brand-dot" cx="370" cy="462" r="7"/><text class="brand-name" x="382" y="470">Plovark</text>
        <circle class="brand-dot" cx="572" cy="462" r="7"/><text class="brand-name" x="584" y="470">Plovark</text>
        <circle class="brand-dot" cx="462" cy="550" r="7"/><text class="brand-name" x="474" y="558">Plovark</text>
        <circle class="brand-dot" cx="572" cy="640" r="7"/><text class="brand-name" x="584" y="648">Plovark</text>
      </g>
    </g>
  </svg>
</main>
</body>
</html>
```